Design for company homepage promoting to the pharmaceutical industry

Our company produces medical education materials and services for the pharmaceutical industry. Our existing website (www.quorvan.net.au) provides more information.
 
We need a homepage design for our new company website we are creating. Our site will not have a great amount of content, we want it to be fast, user friendly and easily adaptable to viewing on any platform, and through any browser. We don't want it over-designed - i.e. no highly animated banner flags, backgrounds, obscure webfonts, too many graphics etc. Attached are files indicating our existing company logo and design. We want the logo and rings to be retained. We've also attached draft copy for the website.
The final website may be designed in Wordpress (still to be confirmed)
 
This is a design to replace the current site (www.quorvan.net.au). Content will also be revised.
Things we don't like about our current design - doesn't use our current branding, is not very exciting, old fashioned 'standard' format, too much content, just doesn't look that good, boring.
 
Examples of sites we like:
www.brelmot.com.au
http://factsheets.wondipaq.com.au/index.html
 
Features we like from these sites - fast, responsive, short and to the point, cross-platform compatible including smartphones, and looks good
 
Main reasons people will visit our site: to find out whether we can provide services they might be looking for, to make a decision on whether they are interested in what we offer so they can get in touch with us, and to get our contact details.
Main thing we want to achieve from website visits is that it looks good enough and provides enough summary information on us so that they want to get in touch with us, to offer us work or to ask us to come in and meet them to provide more info on what we do.
Two most important calls to action from our website
· make the decision that we can do what you are looking for
· get in touch with us.
Updates

Thanks everyone for your submissions. At this stage with the Christmas break upon us, we are yet to finalise our decision, and will make a decision early in the new year. I hope everyone has a good holiday break.
Kind regards
Doug

Target Market(s)

Pharmaceutical industry professionals, marketers and medical professionals.

Industry/Entity Type

Pharmaceutical

Requirements
Must have
• Company logo and rings must be incorporated, company colour - blue - must be in there.
Should not have
• Complex animation or graphics that will slow the upload or limit cross-platform compatability/viewing on smartphones etc.

```html
<!DOCTYPE html>
<html lang="en">
<head>
<meta charset="utf-8">
<title>Quorvan Healthcare Education</title>
<link rel="stylesheet" href="https://fonts.googleapis.com/css2?family=Open+Sans:ital,wght@0,400;0,600;0,700;1,600;1,700&display=swap">
<style>
:root{
  --navy:#0c3a6b;
  --blue:#0a4c86;
  --blue-mid:#1d5f9e;
  --deep:#0b1e36;
  --ink:#333a44;
  --muted:#6b7480;
  --line:#d6dbe1;
  --panel:#e9eaec;
  --grey:#ececec;
  --white:#ffffff;
  --footer:#0d0d0f;
  --link:#1a64ae;
}
*{box-sizing:border-box;margin:0;padding:0}
html,body{width:1200px;height:2875px;overflow:hidden}
body{font-family:"Open Sans",Arial,sans-serif;color:var(--ink);background:var(--white);position:relative}
.wrap{position:absolute;left:138px;width:922px}
h2.section-title{font-size:21px;font-weight:700;color:var(--navy);letter-spacing:-.2px}

/* header */
.site-header{position:absolute;top:0;left:0;width:1200px;height:107px;background:var(--white)}
.brand{position:absolute;left:138px;top:12px;color:var(--navy)}
.brand-name{font-size:44px;font-weight:600;line-height:48px;letter-spacing:-.5px}
.brand-tag{font-size:8px;letter-spacing:1.4px;text-transform:uppercase;margin-left:3px}
.client-login{position:absolute;right:140px;top:0;width:88px;height:29px;background:var(--blue);color:#fff;font-size:12px;display:flex;align-items:center;justify-content:center;border-radius:0 0 3px 3px}
.main-nav{position:absolute;right:140px;top:52px;display:flex;gap:36px;font-size:15.5px;font-weight:600;color:var(--link)}
.main-nav .current{color:var(--deep);border-bottom:2px solid var(--deep);padding-bottom:2px}

/* hero */
.hero{position:absolute;top:107px;left:0;width:1200px;height:340px;background:radial-gradient(ellipse at 50% 55%,#2e6fb4 0%,#0f4b8c 45%,#0a3a70 100%)}
.hero-photo{position:absolute;left:138px;top:0;width:922px;height:340px;
  background:
    radial-gradient(ellipse 160px 200px at 300px 150px,#f0cdb4 0%,rgba(240,205,180,0) 100%),
    radial-gradient(ellipse 190px 230px at 520px 170px,#f3d3bc 0%,rgba(243,211,188,0) 100%),
    radial-gradient(ellipse 130px 190px at 780px 150px,#ead2c2 0%,rgba(234,210,194,0) 100%),
    linear-gradient(90deg,#e9edf1 0%,#f6f2ee 45%,#eef0f3 75%,#e1e6eb 100%)}
.hero-caption{position:absolute;left:696px;top:92px;font-size:28px;line-height:37px;font-weight:700;color:var(--blue);width:300px;text-shadow:0 1px 2px rgba(255,255,255,.8)}
.hero-arrow{position:absolute;top:142px;width:44px;height:44px;background:var(--deep);display:flex;align-items:center;justify-content:center}
.hero-arrow.prev{left:125px}.hero-arrow.next{left:1031px}

/* welcome */
.welcome{top:458px}
.welcome h2{margin-bottom:10px}
.welcome .lead{font-size:13.5px;font-weight:600;color:var(--deep);margin-bottom:6px}
.welcome p{font-size:11.5px;line-height:16px;color:var(--muted)}
.welcome ul{margin:6px 0 4px 10px;list-style:none}
.welcome li{font-size:11.5px;line-height:23px;color:var(--muted)}
.welcome li::before{content:"\2022";margin-right:8px;color:var(--ink)}
.welcome h3{font-size:14px;font-weight:700;color:var(--deep);margin:2px 0 4px}
.btn-small{display:inline-block;margin-top:14px;background:var(--blue-mid);color:#fff;font-size:10px;font-weight:700;font-style:italic;padding:5px 12px}

/* team */
.team{position:absolute;top:751px;left:0;width:1200px;height:286px;background:var(--deep)}
.team h2{position:absolute;left:138px;top:18px;color:#fff;font-size:19px}
.team-row{position:absolute;left:138px;top:64px;display:flex;gap:20px}
.member{width:137px;height:137px;position:relative}
.member.featured{background:linear-gradient(#3a6aa0,#1b4675)}
.member .overlay{position:absolute;left:10px;bottom:14px;color:#fff;font-size:11.5px;font-weight:600;line-height:24px}
.m1{background:radial-gradient(ellipse 34px 42px at 50% 38%,#e3b79b 0%,rgba(227,183,155,0) 100%),linear-gradient(#e7ebef 0%,#e7ebef 55%,#2c2f36 62%,#1d2026 100%)}
.m2{background:radial-gradient(ellipse 30px 38px at 50% 36%,#e9c1a6 0%,rgba(233,193,166,0) 100%),linear-gradient(#f4f4f4 0%,#f4f4f4 55%,#1f2a3d 62%,#18202e 100%)}
.m3{background:radial-gradient(ellipse 32px 40px at 50% 36%,#e0b395 0%,rgba(224,179,149,0) 100%),linear-gradient(#cfd7df 0%,#cfd7df 55%,#6f84a0 62%,#5a6f8a 100%)}
.m4{background:radial-gradient(ellipse 30px 38px at 50% 38%,#eec8ad 0%,rgba(238,200,173,0) 100%),linear-gradient(#eeeeee 0%,#eeeeee 58%,#b8bcc2 64%,#a3a7ad 100%)}
.m5{background:radial-gradient(ellipse 30px 38px at 50% 34%,#8a5a3e 0%,rgba(138,90,62,0) 100%),linear-gradient(#dfe6ee 0%,#dfe6ee 55%,#2d4a78 62%,#233c63 100%)}
.team-note{position:absolute;left:138px;top:213px;width:922px;color:#fff;font-size:11.5px;line-height:16px}

/* services */
.services{position:absolute;top:1037px;left:0;width:1200px;height:383px;background:var(--blue)}
.services h2{position:absolute;left:138px;top:12px;color:#fff;font-size:19px}
.service-grid{position:absolute;left:138px;top:54px;width:922px;display:grid;grid-template-columns:repeat(3,1fr);grid-template-rows:166px 160px}
.service{padding:14px 18px 0 0;position:relative;color:#fff}
.service:nth-child(3n+2),.service:nth-child(3n+3){padding-left:32px;border-left:1px solid rgba(255,255,255,.25)}
.service:nth-child(-n+3){border-bottom:1px solid rgba(255,255,255,.25)}
.service-head{display:flex;align-items:center;gap:14px;height:56px}
.service-head h3{font-size:20px;font-weight:700}
.service p{font-size:11.5px;line-height:17px;margin-top:8px;width:270px}
.find-more{position:absolute;right:40px;bottom:14px;font-size:10.5px;font-style:italic;font-weight:700}

/* work */
.work{top:1432px}
.tabs{display:flex;margin-top:14px}
.tab{width:96px;height:30px;border:1px solid var(--line);border-bottom:none;font-size:13px;display:flex;align-items:center;justify-content:center;color:var(--muted);background:#fff}
.tab.active{background:var(--panel);color:var(--navy);font-weight:700}
.case{background:var(--panel);padding:14px 16px;height:300px}
.case h3{font-size:13px;font-weight:600;color:var(--navy);margin-bottom:12px}
.case p{font-size:11.4px;line-height:18px;color:var(--muted);margin-bottom:12px}
.case strong{color:var(--navy);font-weight:700}

/* testimonials & clients */
.clients-band{position:absolute;top:1808px;left:0;width:1200px;height:475px;background:var(--grey)}
.say{position:absolute;left:138px;top:16px;width:922px}
.say-head{display:flex;justify-content:space-between;align-items:center;border-bottom:2px solid var(--blue-mid);padding-bottom:6px}
.pager{display:flex;gap:2px}
.pager span{width:18px;height:18px;background:var(--blue-mid);display:flex;align-items:center;justify-content:center}
.pager span:first-child{background:#7b8591}
.quote{font-size:12px;line-height:22px;color:var(--ink);margin-top:12px}
.quote .mark{font-size:30px;vertical-align:-10px;color:var(--muted);margin-right:6px}
.clients-title{position:absolute;left:138px;top:142px}
.client-grid{position:absolute;left:138px;top:175px;width:922px;display:grid;grid-template-columns:repeat(4,1fr);grid-template-rows:repeat(3,100px);align-items:center}
.client{display:flex;align-items:center;gap:10px;font-size:21px;font-weight:700;color:#555b63}
.client .sq{width:26px;height:26px;background:#555b63;flex:none}
.client .ci{width:28px;height:28px;border-radius:50%;background:#555b63;flex:none}

/* contact */
.contact-bar{position:absolute;top:2283px;left:0;width:1200px;height:54px;background:var(--blue)}
.contact-bar h2{position:absolute;left:138px;top:13px;color:#fff;font-size:19px}
.map{position:absolute;top:2337px;left:0;width:1200px;height:431px;
  background:
    radial-gradient(ellipse 300px 200px at 30% 40%,#d4d4d4 0%,rgba(212,212,212,0) 100%),
    radial-gradient(ellipse 260px 180px at 75% 65%,#d0d0d0 0%,rgba(208,208,208,0) 100%),
    linear-gradient(135deg,#e6e6e6,#dadada 50%,#e3e3e3)}

/* footer */
.site-footer{position:absolute;top:2768px;left:0;width:1200px;height:107px;background:var(--footer);color:#bfc3c8;font-size:11.5px;line-height:21px}
.foot-address{position:absolute;left:138px;top:18px}
.foot-contact{position:absolute;left:370px;top:18px}
.foot-contact b{color:#3c8fe0;font-weight:400}
.social{position:absolute;right:140px;top:20px;display:flex;gap:8px}
.social span{width:22px;height:22px;background:#2f7bc6}
.copyright{position:absolute;right:140px;top:62px;color:#7f868e}
</style>
</head>
<body>

<header class="site-header">
  <div class="brand">
    <div class="brand-name">quorvan</div>
    <div class="brand-tag">Healthcare Education</div>
  </div>
  <a class="client-login">Client Login</a>
  <nav class="main-nav">
    <span class="current">Home</span><span>Who we are</span><span>What we do</span><span>Some of our work</span><span>Who we work with</span><span>Contact us</span>
  </nav>
</header>

<section class="hero">
  <div class="hero-photo" role="img" aria-label="Photo of a smiling doctor with a young girl and her mother"></div>
  <div class="hero-caption">Lorem ipsum dolor sit amet consectetur adipiscing</div>
  <div class="hero-arrow prev"><svg width="14" height="20" viewBox="0 0 14 20"><path d="M11 2 3 10l8 8" fill="none" stroke="#fff" stroke-width="3"/></svg></div>
  <div class="hero-arrow next"><svg width="14" height="20" viewBox="0 0 14 20"><path d="M3 2l8 8-8 8" fill="none" stroke="#fff" stroke-width="3"/></svg></div>
</section>

<section class="wrap welcome">
  <h2 class="section-title">Welcome To Quorvan</h2>
  <p class="lead">At Quorvan we are healthcare communication specialists; this means we're scientists, journalists and marketers rolled into one.</p>
  <p>As you can see we provide all the things you'd expect from a top-class healthcare communications agency, but we have the depth of technical understanding and creative flair to produce sophisticated and memorable materials and programs, including:</p>
  <ul>
    <li>Strategic tools for brand promotion (such as detail aids, product monographs, slide kits and patient materials)</li>
    <li>Non-promotional materials for market education (e.g. clinical papers and evidence summaries)</li>
    <li>Complex programs such as clinical audits and product familiarisation programs</li>
    <li>Medical meetings and symposia</li>
  </ul>
  <h3>Looking for something different pre-launch?</h3>
  <p>Quorvan have developed a unique tool for the online management of drug delivery, ideal for implementation in early access and special needs programs.</p>
  <span class="btn-small">Learn More</span>
</section>

<section class="team">
  <h2 class="section-title">The Quorvan Team</h2>
  <div class="team-row">
    <div class="member featured" role="img" aria-label="Portrait of the managing director">
      <div class="overlay">Doug Hartwell<br>Managing Director</div>
    </div>
    <div class="member m1" role="img" aria-label="Portrait of a team member"></div>
    <div class="member m2" role="img" aria-label="Portrait of a team member"></div>
    <div class="member m3" role="img" aria-label="Portrait of a team member"></div>
    <div class="member m4" role="img" aria-label="Portrait of a team member"></div>
    <div class="member m5" role="img" aria-label="Portrait of a team member"></div>
  </div>
  <p class="team-note">Doug Hartwell Managing Director and all members of our in-house team of project managers, medical writers, designers, administration and production staff are dedicated to delivery on time, on budget, and beyond expectations.<br>We are proud of what we do.</p>
</section>

<section class="services">
  <h2 class="section-title">What we do</h2>
  <div class="service-grid">
    <div class="service">
      <div class="service-head"><svg width="26" height="40" viewBox="0 0 26 40" fill="#fff"><circle cx="14" cy="5" r="4.5"/><path d="M10 11h7l3 10 5 3-1 3-7-4-1-3-2 8 5 6 1 6h-4l-1-5-6-6-2 11H3l3-17 1-6-3 3v6H1v-8z"/></svg><h3>Promotion</h3></div>
      <p>Quorvan can help you promote your brand – from the development of strategic communication campaigns to the creation of discrete....</p>
      <span class="find-more">Find Out More &raquo;</span>
    </div>
    <div class="service">
      <div class="service-head"><svg width="28" height="40" viewBox="0 0 28 40"><rect x="6" y="1" width="20" height="34" fill="#fff"/><rect x="2" y="5" width="20" height="34" fill="#fff" stroke="#0a4c86" stroke-width="2"/></svg><h3>Education</h3></div>
      <p>Clinical papers, evidence summaries, scientific newsletters and accredited educational materials are among the supporting materials</p>
      <span class="find-more">Find Out More &raquo;</span>
    </div>
    <div class="service">
      <div class="service-head"><svg width="40" height="40" viewBox="0 0 40 40"><rect x="2" y="5" width="36" height="33" fill="#fff"/><rect x="2" y="5" width="36" height="8" fill="#fff" stroke="#0a4c86" stroke-width="1"/><rect x="9" y="1" width="4" height="8" fill="#fff"/><rect x="27" y="1" width="4" height="8" fill="#fff"/><text x="20" y="33" text-anchor="middle" font-family="Open Sans,sans-serif" font-weight="700" font-size="17" fill="#0a4c86">17</text></svg><h3>Promotion</h3></div>
      <p>From clinical audits to patient support activities, Quorvan has the experience to successfully develop</p>
      <span class="find-more">Find Out More &raquo;</span>
    </div>
    <div class="service">
      <div class="service-head"><svg width="44" height="32" viewBox="0 0 44 32" fill="#fff"><circle cx="11" cy="7" r="5"/><circle cx="33" cy="7" r="5"/><circle cx="22" cy="11" r="6"/><path d="M2 24q0-9 9-9t9 9zM24 24q0-9 9-9t9 9z"/><path d="M10 32q0-12 12-12t12 12z"/></svg><h3>Meetings</h3></div>
      <p>You will maximise your investment in scientific meetings by employing Quorvan to manage the entire process from concept</p>
      <span class="find-more">Find Out More &raquo;</span>
    </div>
    <div class="service">
      <div class="service-head"><svg width="40" height="40" viewBox="0 0 40 40"><g fill="#fff"><circle cx="20" cy="20" r="12"/><rect x="17" y="1" width="6" height="38"/><rect x="1" y="17" width="38" height="6"/><rect x="17" y="1" width="6" height="38" transform="rotate(45 20 20)"/><rect x="17" y="1" width="6" height="38" transform="rotate(-45 20 20)"/></g><circle cx="20" cy="20" r="5" fill="#0a4c86"/></svg><h3>IME</h3></div>
      <p>Clinical papers, evidence summaries, scientific newsletters and accredited educational materials are among the supporting</p>
      <span class="find-more">Find Out More &raquo;</span>
    </div>
    <div class="service">
      <div class="service-head"><svg width="36" height="40" viewBox="0 0 36 40" fill="none" stroke="#fff" stroke-width="3"><path d="M4 2v10q0 10 9 10t9-10V2"/><path d="M13 22v6q0 9 9 9t9-9v-6"/><circle cx="31" cy="18" r="3.5" fill="#fff"/></svg><h3>Healthcare</h3></div>
      <p>Clinical papers, evidence summaries, scientific newsletters and accredited educational materials are among the supporting materials</p>
      <span class="find-more">Find Out More &raquo;</span>
    </div>
  </div>
</section>

<section class="wrap work">
  <h2 class="section-title">Some of our work</h2>
  <div class="tabs"><span class="tab active">Case 1</span><span class="tab">Case 2</span><span class="tab">Case 3</span><span class="tab">Case 4</span></div>
  <div class="case">
    <h3>The Cardiovascular Symposium 2008</h3>
    <p><strong>THE CHALLENGE:</strong> In 2007, following on from the success of the Cardivex Institute which initially focused more on providing largely business-based content to a broad range of Australian GPs, our client asked us to create a meeting focusing directly on cardiovascular topics. This move was successful, and, based on the largely positive feedback from 2007, the aim for 2008 was to build on this progress and extend the program to include four meetings in four states.</p>
    <p><strong>SOLUTION:</strong> Each symposium offered a combination of plenary lectures, interactive case discussions, small-group workshops and interactive thought-provoker sessions. As an NCGP-accredited provider of Continuing Professional Development (CPD) programs, Quorvan ensured attendees qualified for 40 (Category 1) QA&amp;CPD points. We managed all aspects of content development and meeting delivery, covering the formation and management of a steering committee, agenda development with specific learning objectives, speaker recruitment and liaison, slide and content management and on-site audio-visual and presentation management. Our in-house writing, design and production team created all supporting materials.</p>
    <p><strong>RESULTS:</strong> Delegate feedback demonstrated that the meetings were a valuable learning experience. Many delegates commented on the quality of the content of the presentations and were impressed by the high level of interactivity that was achieved at such a large meeting. Delegates also commented on the practical advice that was offered, which kept the activity relevant, highly appropriate and applicable.</p>
  </div>
</section>

<section class="clients-band">
  <div class="say">
    <div class="say-head">
      <h2 class="section-title">What Our Cleitns are Saying</h2>
      <div class="pager">
        <span><svg width="8" height="10" viewBox="0 0 8 10"><path d="M6 1 2 5l4 4" fill="none" stroke="#fff" stroke-width="2"/></svg></span>
        <span><svg width="8" height="10" viewBox="0 0 8 10"><path d="M2 1l4 4-4 4" fill="none" stroke="#fff" stroke-width="2"/></svg></span>
      </div>
    </div>
    <p class="quote"><span class="mark">&ldquo;</span>Congratulations &amp; many thanks for your seriously wonderful &amp; successful work on the weekend. I'm especially grateful for the calm, cool &amp; very clever work done in managing all the planning process before I even came on board – truly outstanding</p>
  </div>
  <h2 class="section-title clients-title">What Our Cleitns are Saying</h2>
  <div class="client-grid">
    <div class="client">Veltramed</div>
    <div class="client"><span class="sq"></span>Orrinox</div>
    <div class="client">Castiva</div>
    <div class="client">Bryvel</div>
    <div class="client" style="font-size:15px"><span class="ci"></span>Tollen-Marsh Labs</div>
    <div class="client"><span class="ci"></span>Quendra</div>
    <div class="client" style="font-size:18px"><span class="sq"></span>Halvorn-Dace</div>
    <div class="client">Mirelle</div>
    <div class="client" style="font-size:18px"><span class="ci"></span>Stavrik Pharma</div>
    <div class="client" style="font-size:19px">Lumeris Pharma</div>
    <div class="client">Pentavo</div>
    <div class="client">Corvane</div>
  </div>
</section>

<section class="contact-bar"><h2 class="section-title">Have an idea ? Get in Touch</h2></section>
<div class="map" role="img" aria-label="Street map of the office neighbourhood"></div>

<footer class="site-footer">
  <div class="foot-address">Quorvan Healthcare Education<br>Level 3, 18 Marlow Street<br>Northbridge NSW 2063, Australia</div>
  <div class="foot-contact"><b>Call :</b> + 61 2 9000 4127<br><b>Fax :</b> + 61 2 9000 4128<br><b>Email :</b> info@quorvan.net.au</div>
  <div class="social" aria-label="Social links"><span></span><span></span><span></span><span></span><span></span><span></span><span></span></div>
  <div class="copyright">Copyright (c) 2013 Quorvan Healthcare Education</div>
</footer>

</body>
</html>
```